TWR Business Card Design

As a full service media and advocacy firm, we lean on years of experience in political and corporate consulting, grassroots campaigning, media placement, and video production to deliver unparalleled results. Recently we have moved into digital media and now provide this service for our clients.

I will add our two company logos to be used on the business cards. The longer logo with "sky reach studio" is our primary logo. Our secondary logo is more square one with "sky reach" and 'digital.media.campaigns" on it. We are looking for clean and modern looking business cards fitting for a digital firm.

I will also add our logos that go well with dark backgrounds.

Industry/Entity Type

Political

Contact Information for Business Card

Walter Pennick, Director of Campaigns and Digital, 555-218-4760, walter@skyreachstudioco.example, @SkyReachStudioCo, @WalterPennick, Facebook.com/SkyReachStudioCo

```html
<!DOCTYPE html>
<html lang="en">
<head>
<meta charset="utf-8">
<title>Sky Reach Studio – Business Card</title>
<link rel="stylesheet" href="https://fonts.googleapis.com/css2?family=Lato:wght@400;700;900&display=swap">
<style>
  :root {
    --stage: #2a2a2a;
    --card: #fbfbfb;
    --brand-blue: #1b86d6;
    --navy: #1a2c78;
    --ink: #1d1d22;
    --white: #ffffff;
  }
  * { margin: 0; padding: 0; box-sizing: border-box; }
  html, body {
    width: 1200px;
    height: 873px;
    overflow: hidden;
    background: var(--stage);
    font-family: "Lato", Arial, sans-serif;
  }
  .business-card {
    position: absolute;
    left: 180px;
    top: 196px;
    width: 840px;
    height: 480px;
    background: var(--card);
    overflow: hidden;
  }
  .brand-name {
    position: absolute;
    left: 54px;
    top: 52px;
    font-size: 50px;
    font-weight: 700;
    letter-spacing: 1px;
    color: var(--brand-blue);
    line-height: 1;
  }
  .person-name {
    position: absolute;
    right: 54px;
    top: 150px;
    font-size: 26px;
    font-weight: 700;
    color: var(--brand-blue);
  }
  .divider {
    position: absolute;
    left: 50px;
    right: 50px;
    top: 192px;
    height: 3px;
    background: var(--navy);
  }
  .person-title {
    position: absolute;
    right: 54px;
    top: 204px;
    font-size: 17px;
    color: var(--ink);
  }
  .contact-list, .social-list {
    position: absolute;
    list-style: none;
  }
  .contact-list { left: 54px; top: 300px; }
  .social-list { left: 452px; top: 246px; }
  .contact-item {
    display: flex;
    align-items: center;
    gap: 12px;
    height: 36px;
    font-size: 19px;
    color: var(--ink);
  }
  .icon-dot {
    width: 26px;
    height: 26px;
    border-radius: 50%;
    background: var(--brand-blue);
    flex: none;
    display: flex;
    align-items: center;
    justify-content: center;
  }
  .icon-dot svg { width: 16px; height: 16px; }
  .card-footer {
    position: absolute;
    left: 0;
    bottom: 0;
    width: 840px;
    height: 110px;
  }
</style>
</head>
<body>
  <main class="business-card">
    <div class="brand-name">SKY REACH STUDIO</div>

    <div class="person-name">Walter Pennick</div>
    <div class="divider"></div>
    <div class="person-title">Director of Campaigns and Digital</div>

    <ul class="social-list">
      <li class="contact-item"><span class="icon-dot"></span>Instagram.com/@SkyReachStudioCo</li>
      <li class="contact-item"><span class="icon-dot"></span>twitter.com/@WalterPennick</li>
      <li class="contact-item"><span class="icon-dot"></span>Facebook.com/SkyReachStudioCo</li>
    </ul>

    <ul class="contact-list">
      <li class="contact-item">
        <span class="icon-dot">
          <svg viewBox="0 0 16 16"><path fill="var(--white)" d="M3 2h3l1 3-2 1c1 2 2 3 4 4l1-2 3 1v3c0 1-1 2-2 2C6 14 2 10 2 4c0-1 0-2 1-2z"/></svg>
        </span>555-218-4760
      </li>
      <li class="contact-item">
        <span class="icon-dot">
          <svg viewBox="0 0 16 16"><rect x="2" y="4" width="12" height="8" fill="none" stroke="var(--white)" stroke-width="1.5"/><polyline points="2,4 8,9 14,4" fill="none" stroke="var(--white)" stroke-width="1.5"/></svg>
        </span>walter@skyreachstudioco.example
      </li>
      <li class="contact-item">
        <span class="icon-dot">
          <svg viewBox="0 0 16 16"><g fill="none" stroke="var(--white)" stroke-width="1.6"><rect x="2" y="6" width="7" height="4" rx="2" transform="rotate(-45 5.5 8)"/><rect x="7" y="6" width="7" height="4" rx="2" transform="rotate(-45 10.5 8)"/></g></svg>
        </span>www.skyreachstudioco.example
      </li>
    </ul>

    <svg class="card-footer" viewBox="0 0 840 110" aria-hidden="true">
      <path fill="var(--brand-blue)" d="M0 86 H520 C545 86 552 74 575 74 H840 V110 H0 Z"/>
      <path fill="var(--navy)" stroke="var(--card)" stroke-width="5" d="M548 112 C575 112 585 52 625 52 H845 V112 Z"/>
    </svg>
  </main>
</body>
</html>
```